Business Card Design Project - Small Bar

We would like a design for a business card for our new small bar in Melbourne. It is quite the 'hipster' bar and the card would need to reflect this in its design. We do have a logo which needs to be used in the card, tho how it is incorporated is up to you! :)

OK, the Bar currently has a common 'inner city' vibe, i.e. random artwork, older 30s/40's club furniture, grafitti murals on the walls, eclectic objects etc etc Current clientele would be described as "hipster", "urban professional" etc. How to describe... they are 30, have a good job but have beards, beanies and own vinyl records. :)

The card will be used to give to professional contacts and to bands/solo artists we come across to invite them to come play at our venue, so somehow I would like it to convey the image of 'professional' and 'funky' all in one. Difficult I know.

I have asked for some advice on making this brief clearer, so check back.

Thanks all in advance. :)
Updates

Sorry all

I've now been told that it is WEST MELBOURNE 3003. Apparently we are on the border and it is referred to by either west or north Melbourne, but it is definitely West Melbourne 3003.

Things you learn hey? :)

Target Market(s)

Hipsters, urbanites, the inner city crowd

Industry/Entity Type

Artists

Requirements
Must have
Name of the bar "The Lantern & Badger"
Address - 128 Pembury St, North Melbourne, Victoria 3051
Names - Paul Redfern, Dean Horwick
mobile. 0417265930 and 0439572614
Obviously we would need separate cards?
Nice to have
• Gigboard link
Gigboard 'like' icon
Should not have
• traditional designs. I am looking for something unique and funky. with FUNK! :)

```html
<!DOCTYPE html>
<html lang="en">
<head>
<meta charset="utf-8">
<title>The Lantern &amp; Badger – Business Card</title>
<link href="https://fonts.googleapis.com/css2?family=Handlee&family=Questrial&display=swap" rel="stylesheet">
<style>
  :root {
    --page-bg: #e9e6e2;
    --card-bg: #2a2627;
    --band: #f07a2a;
    --white: #ffffff;
    --pink: #e84fa8;
    --yellow: #f2ea1d;
    --orange: #f07a2a;
    --green: #8fb33a;
    --chip-bg: #ffffff;
    --chip-ink: #2a2627;
    --chip-mark: #f07a2a;
  }
  * { box-sizing: border-box; margin: 0; padding: 0; }
  html, body {
    width: 1200px;
    height: 872px;
    overflow: hidden;
    background: var(--page-bg);
  }
  .business-card {
    position: absolute;
    left: 100px;
    top: 130px;
    width: 1000px;
    height: 611px;
    background: var(--card-bg);
    box-shadow: 0 10px 30px rgba(0,0,0,0.25);
    font-family: "Questrial", sans-serif;
  }
  .mascot-row {
    position: absolute;
    left: 0;
    top: 70px;
    width: 100%;
    display: flex;
    justify-content: space-around;
    padding: 0 40px;
  }
  .mascot-mark {
    width: 170px;
    height: 120px;
    display: flex;
    align-items: center;
    justify-content: center;
    text-align: center;
    font-size: 24px;
    line-height: 1.2;
  }
  .mascot-mark--pink { color: var(--pink); }
  .mascot-mark--yellow { color: var(--yellow); }
  .mascot-mark--orange { color: var(--orange); }
  .mascot-mark--green { color: var(--green); }
  .name-band {
    position: absolute;
    left: 0;
    top: 262px;
    width: 100%;
    height: 110px;
    background: var(--band);
    display: flex;
    align-items: center;
    justify-content: center;
  }
  .bar-name {
    font-family: "Handlee", cursive;
    font-size: 74px;
    font-weight: 400;
    color: var(--white);
    letter-spacing: 1px;
  }
  .like-chip {
    position: absolute;
    right: 26px;
    top: 392px;
    height: 30px;
    padding: 0 8px;
    background: var(--chip-bg);
    border-radius: 3px;
    display: flex;
    align-items: center;
    gap: 6px;
    font-size: 15px;
    color: var(--chip-ink);
  }
  .chip-mark {
    flex: none;
    width: 12px;
    height: 12px;
    border-radius: 50%;
    background: var(--chip-mark);
  }
  .contact {
    position: absolute;
    left: 150px;
    top: 452px;
    text-transform: uppercase;
  }
  .contact-line {
    font-size: 30px;
    letter-spacing: 1px;
  }
  .contact-name { color: var(--green); margin-right: 22px; }
  .contact-phone { color: var(--pink); }
  .contact-address {
    margin-top: 10px;
    font-size: 26px;
    color: var(--white);
    letter-spacing: 0.5px;
  }
  .social-chip {
    position: absolute;
    left: 24px;
    bottom: 22px;
    width: 110px;
    height: 36px;
    background: var(--chip-bg);
    border-radius: 3px;
    display: flex;
    align-items: center;
    gap: 6px;
    padding: 0 6px;
    color: var(--chip-ink);
    font-size: 10px;
    line-height: 1.1;
  }
  .social-chip .chip-mark {
    width: 16px;
    height: 16px;
  }
</style>
</head>
<body>
  <div class="business-card">
    <div class="mascot-row">
      <div class="mascot-mark mascot-mark--pink">Lantern &amp;<br>Badger</div>
      <div class="mascot-mark mascot-mark--yellow">Lantern &amp;<br>Badger</div>
      <div class="mascot-mark mascot-mark--orange">Lantern &amp;<br>Badger</div>
      <div class="mascot-mark mascot-mark--green">Lantern &amp;<br>Badger</div>
    </div>

    <div class="name-band">
      <h1 class="bar-name">The Lantern &amp; Badger</h1>
    </div>

    <div class="like-chip"><span class="chip-mark"></span>Like</div>

    <div class="contact">
      <p class="contact-line">
        <span class="contact-name">Paul Redfern</span>
        <span class="contact-phone">T: 0417265930</span>
      </p>
      <p class="contact-address">128 Pembury St, North Melbourne, Victoria 3051</p>
    </div>

    <div class="social-chip">
      <span class="chip-mark"></span>
      <span>Find us on<br>Gigboard</span>
    </div>
  </div>
</body>
</html>
```